GRape Crate Society Business Card design

Create a new business card that is contemporary but maintains the air of wine and the logo's history. I have put the original logo and a more current logo. The element we would like to keep intact is the visual the two gentleman holding the wine glasses...however, if there is an interesting interpretation of these two figures, have at it.

the company name is:

The Heritage Grape Crate Society
457 E. Larkspur Ave.
Alderbrook, CA 90412
800-555-0173

```html
<!DOCTYPE html>
<html lang="en">
<head>
<meta charset="utf-8">
<title>Grape Crate Society Business Card</title>
<link rel="stylesheet" href="https://fonts.googleapis.com/css2?family=Lobster&display=swap">
<style>
  :root {
    --backdrop: #2e2f2e;
    --wine: #921b32;
    --wine-soft: #c96b7e;
    --grape: #e6b3bd;
    --leaf: #dfe6d8;
    --paper: #f7f5f5;
    --white: #ffffff;
  }
  * { margin: 0; padding: 0; box-sizing: border-box; }
  html, body { width: 1200px; height: 894px; overflow: hidden; }
  body {
    background: var(--backdrop);
    font-family: "Lobster", cursive;
    position: relative;
  }
  .card {
    position: absolute;
    width: 640px;
    height: 366px;
    left: 280px;
    border-radius: 4px;
    overflow: hidden;
    box-shadow: 0 6px 18px rgba(0,0,0,.45);
  }
  .card-back { top: 51px; background: var(--wine); }
  .card-front { top: 477px; background: var(--paper); }

  .back-name {
    position: absolute;
    inset: 0;
    display: flex;
    align-items: center;
    justify-content: center;
    text-align: center;
    color: var(--white);
    font-size: 34px;
    line-height: 1.15;
  }

  .grapes {
    position: absolute;
    top: 0; right: 30px;
    width: 200px; height: 200px;
    border-radius: 0 0 50% 50%;
    background: linear-gradient(180deg, var(--leaf) 0%, var(--grape) 35%, #d994a3 100%);
    opacity: .7;
  }
  .splatter {
    position: absolute;
    right: -30px; top: 150px;
    width: 260px; height: 200px;
    border-radius: 50%;
    background: radial-gradient(ellipse at 55% 45%, rgba(146,27,50,.7) 0%, rgba(201,107,126,.4) 45%, rgba(247,245,245,0) 72%);
  }
  .company-title {
    position: absolute;
    top: 30px; left: 40px;
    width: 520px;
    text-align: center;
    color: var(--wine);
    font-size: 38px;
    font-weight: 400;
    line-height: 1.15;
  }
  .company-title span { display: block; }
  .brand-badge {
    position: absolute;
    left: 42px; top: 168px;
    width: 170px; height: 170px;
    border-radius: 50%;
    background: var(--wine);
    color: var(--white);
    display: flex;
    align-items: center;
    justify-content: center;
    text-align: center;
    font-size: 20px;
    line-height: 1.15;
    padding: 22px;
  }
  .contact {
    position: absolute;
    left: 236px; top: 200px;
    list-style: none;
    color: var(--wine);
    font-size: 24px;
    line-height: 1.25;
  }
  .contact li { display: flex; align-items: flex-start; gap: 10px; margin-bottom: 6px; }
  .contact svg { flex: none; margin-top: 6px; }
</style>
</head>
<body>
  <section class="card card-back">
    <p class="back-name">Grape Crate<br>Society</p>
  </section>

  <section class="card card-front">
    <div class="grapes" role="img" aria-label="Cluster of pink grapes with a pale leaf"></div>
    <div class="splatter" role="img" aria-label="Red wine watercolour splash"></div>

    <h1 class="company-title"><span>The Heritage</span><span>Grape Crate Society</span></h1>

    <div class="brand-badge">Grape Crate Society</div>

    <ul class="contact">
      <li>
        <svg width="18" height="18" viewBox="0 0 18 18" aria-hidden="true">
          <circle cx="9" cy="9" r="9" fill="var(--wine)"/>
          <path d="M9 4a3.2 3.2 0 0 0-3.2 3.2C5.8 9.6 9 14 9 14s3.2-4.4 3.2-6.8A3.2 3.2 0 0 0 9 4z" fill="var(--white)"/>
          <circle cx="9" cy="7.2" r="1.2" fill="var(--wine)"/>
        </svg>
        <span>457 E. Larkspur Ave.<br>Alderbrook, CA 90412</span>
      </li>
      <li>
        <svg width="18" height="18" viewBox="0 0 18 18" aria-hidden="true">
          <circle cx="9" cy="9" r="9" fill="var(--wine)"/>
          <path d="M6 4.8l1.6-.4 1 2.3-1 .8a6 6 0 0 0 2.9 2.9l.8-1 2.3 1-.4 1.6c-3.8.3-7.5-3.4-7.2-7.2z" fill="var(--white)"/>
        </svg>
        <span>800-555-0173</span>
      </li>
    </ul>
  </section>
</body>
</html>
```